Stationary Design for an engineering start-up.

Company name: Calvenor Plank Inc.

Our advanced materials company utilizes a patented process to spray-coat wood surfaces with metal. Metal is sprayed as a super-heated powder and fully conforms to the surface of the wood allowing for a wide range of applications. Metals used are COPPER and BRONZE.

We need a stationary package that includes Business Card, Letter Head, and Envelope.

- After we will submit a contest for a brochure design, so a winning designer will have advantage to take that project as well.

Target Market(s)

Our target market are building and industrial design professionals.

- Architects
- Designers
- Builders

Industry/Entity Type

Engineering

Requirements
Must have
• - All stationary must include our logo (attached)

Sizes:
Business card: Standard 3.5 by 2 inches. Landscape.

Letterhead: 8.5" x 11"

Envelopes:
One standard commercial size #10 (4 1/8" by 9 1/2")
One catalog size envelope (9" by 12")
Assume envelopes are one-sided (front print only)

- Use bleeds where applicable

- Include all fonts used.

File Format:
AI or PSD
** for letterhead please include MSWord template.
Nice to have
• Design style
- Take design style from our logo and attached images.
- Modern, sharp, minimalistic
- Sans fonts
- Don''t be afraid to use color background for business card.
We''re open to ideas of making the business card somehow representative of the product - metal coated wood.

```html
<!DOCTYPE html>
<html lang="en">
<head>
<meta charset="utf-8">
<title>Calvenor Plank Inc. — Stationery</title>
<link href="https://fonts.googleapis.com/css2?family=Lato:wght@400&display=swap" rel="stylesheet">
<style>
:root{
  --bg:#ece9e2;
  --red:#bf2e1e;
  --orange:#e8532a;
  --tan:#c3b59b;
  --cream:#fdfdeb;
  --panel:#f1f0d4;
  --ink:#1c1c1c;
  --copy:#3a3a3a;
  --white:#ffffff;
  --rule:#8a8a80;
}
*{margin:0;padding:0;box-sizing:border-box}
html,body{width:1200px;height:842px;overflow:hidden}
body{background:var(--bg);position:relative;font-family:"Lato",sans-serif;color:var(--ink)}
.piece{position:absolute;box-shadow:0 6px 14px rgba(0,0,0,.25)}
.brand{display:flex;align-items:center;gap:10px;position:absolute}
.brand-mark{background:var(--red);flex:none}
.brand-name{font-weight:400;color:var(--ink);letter-spacing:.22em;line-height:1;white-space:nowrap}
.band{position:absolute;left:0;top:0;bottom:0;background:var(--red)}
.band-top{position:absolute;left:0;top:0;width:100%;background:var(--tan)}
.band-tip{position:absolute;bottom:0;right:0;width:30%;background:var(--orange)}
.panel{position:absolute;right:0;bottom:0;background:var(--panel)}
.address{position:absolute;font-size:6.5px;line-height:9.8px;color:var(--copy);white-space:nowrap}
.address .web{color:var(--red)}

/* logo sheet */
.logo-sheet{left:66px;top:69px;width:519px;height:680px;background:var(--white)}
.logo-stacked{position:absolute;left:28px;top:50px;width:180px;text-align:center}
.logo-stacked .brand-mark{width:46px;height:46px;margin:0 auto 14px}
.logo-stacked .brand-name{font-size:25px}
.logo-sheet .brand.horizontal{left:235px;top:74px}
.logo-sheet .brand.horizontal .brand-mark{width:40px;height:40px}
.logo-sheet .brand.horizontal .brand-name{font-size:25px}

/* envelope */
.envelope{left:91px;top:279px;width:457px;height:237px}
.envelope-flap{position:absolute;left:0;top:0;width:457px;height:39px;background:var(--red);clip-path:polygon(3% 0,97% 0,100% 100%,0 100%)}
.envelope-body{position:absolute;left:0;top:39px;width:457px;height:198px;background:var(--cream)}
.envelope-body .band{width:14px}
.envelope-body .band-top{height:23px}
.envelope-body .band-tip{height:22px}
.envelope-body .brand{left:32px;top:22px}
.envelope-body .brand-mark{width:32px;height:32px}
.envelope-body .brand-name{font-size:20px}
.envelope-body .panel{left:97px;top:71px}
.envelope-body .address{left:30px;top:75px}
.envelope-window{position:absolute;left:281px;top:124px;width:153px;height:42px;background:var(--white);border-radius:10px}

/* compliments slip */
.compliments{left:87px;top:570px;width:457px;height:199px;background:var(--cream)}
.compliments .band{width:14px}
.compliments .band-top{height:24px}
.compliments .band-tip{height:22px}
.compliments .brand{left:26px;top:30px}
.compliments .brand-mark{width:32px;height:32px}
.compliments .brand-name{font-size:20px}
.compliments-label{position:absolute;right:9px;top:31px;font-size:9px;color:var(--ink)}
.compliments-rule{position:absolute;left:216px;right:0;top:49px;height:1px;background:var(--rule)}
.compliments .panel{left:96px;top:72px}
.compliments .address{left:28px;top:83px}

/* letterhead */
.letterhead{left:584px;top:41px;width:543px;height:739px;background:var(--cream)}
.letterhead .band{width:22px}
.letterhead .band-top{height:90px}
.letterhead .band-tip{height:22px;width:25%}
.letterhead .brand{left:49px;top:25px}
.letterhead .brand-mark{width:44px;height:44px}
.letterhead .brand-name{font-size:27px}
.letterhead .panel{left:124px;top:91px}
.letterhead .address{left:45px;top:102px}

/* business card */
.business-card{left:884px;top:338px;width:268px;height:152px;overflow:hidden;
  background:linear-gradient(100deg,#8c5a3c 0%,#b27a55 35%,#d89a6c 60%,#a66c48 100%)}
.card-grain{position:absolute;inset:0;clip-path:polygon(71% 0,100% 0,100% 100%,93% 100%,88% 60%);
  background:linear-gradient(160deg,#e8c99a,#c99a64 45%,#f1d7ad 70%,#b98251)}
.business-card .brand{left:10px;top:13px}
.business-card .brand-mark{width:28px;height:28px}
.business-card .brand-name{font-size:19px;color:var(--ink)}
.business-card .address{left:16px;top:58px;font-size:6px;color:#3b2216}
.business-card .address .web{color:#f3e1cc}
.card-holder{position:absolute;left:109px;top:77px;font-size:12px;color:#1e120b;white-space:nowrap}
</style>
</head>
<body>

<section class="piece logo-sheet">
  <div class="logo-stacked">
    <div class="brand-mark"></div>
    <div class="brand-name">CALVENOR</div>
  </div>
  <div class="brand horizontal">
    <div class="brand-mark"></div>
    <div class="brand-name">CALVENOR</div>
  </div>
</section>

<section class="piece envelope">
  <div class="envelope-flap"></div>
  <div class="envelope-body">
    <div class="band"><div class="band-top"></div><div class="band-tip"></div></div>
    <div class="brand"><div class="brand-mark"></div><div class="brand-name">CALVENOR</div></div>
    <div class="panel"></div>
    <div class="address">Calvenor Plank Inc.<br>48 Mill Road<br>Alderbrook<br>Province<br>K7P 2R9</div>
    <div class="envelope-window"></div>
  </div>
</section>

<section class="piece compliments">
  <div class="band"><div class="band-top"></div><div class="band-tip"></div></div>
  <div class="brand"><div class="brand-mark"></div><div class="brand-name">CALVENOR</div></div>
  <div class="compliments-label">With Compliments</div>
  <div class="compliments-rule"></div>
  <div class="panel"></div>
  <div class="address">Calvenor Plank Inc.<br>48 Mill Road<br>Alderbrook<br>Province<br>K7P 2R9<br>t. 555.018.2746<br>f. 555.018.2747<br><span class="web">www.calvenorplank.com</span></div>
</section>

<section class="piece letterhead">
  <div class="band"><div class="band-top"></div><div class="band-tip"></div></div>
  <div class="brand"><div class="brand-mark"></div><div class="brand-name">CALVENOR</div></div>
  <div class="panel"></div>
  <div class="address">Calvenor Plank Inc.<br>48 Mill Road<br>Alderbrook<br>Province<br>K7P 2R9<br>t. 555.018.2746<br>f. 555.018.2747<br><span class="web">www.calvenorplank.com</span></div>
</section>

<section class="piece business-card">
  <div class="card-grain" role="img" aria-label="Metal-coated wood grain texture"></div>
  <div class="brand"><div class="brand-mark"></div><div class="brand-name">CALVENOR</div></div>
  <div class="address">Calvenor Plank Inc.<br>48 Mill Road<br>Alderbrook<br>Province<br>K7P 2R9<br>t. 555.018.2746<br>f. 555.018.2747<br><span class="web">www.calvenorplank.com</span></div>
  <div class="card-holder">Mara Lindqvist</div>
</section>

</body>
</html>
```